Buch-/eBook-Cover für Autobiografie
Das Disign von dem Cover hat mir auf Anhieb sehr gut gefallen. Das hat gleich "ins schwarze" getroffen. Die Kommunikation war effizient und zielgerichtet
Zielgruppe
Ich bin eine Privatperson und habe im Laufe der letzten Jahre mein Autobiografie geschrieben. Besser gesagt ist es ein autobiografischer Roman geworden. Ich plane dieses Buch meiner Frau und meinen Söhnen und deren Familien zu schenken. Darüber hinaus ist es aber auch geplant das Buch bei Bravoria zu veröffentlichen.
Aufgabenstellung
Auf dem Cover sollte neben meinem Namen Rupert(a) Hallmann natürlich auch der Titel von dem Buch stehen. Ich habe dem Buch den Titel gegeben: 'Das Licht am Ufer'. Auf dem Backcover hatte ich mir eine kurze zusammenfassung vorgestellt, die ich auch beifüge. Ich hatte geplant, das sowohl auf dem Cover, wie auch auf dem Backcover Bilder von mir (u.a. als Baby) mit gestaltet werden. Aber das ist nur so eine Idee, ich bin da für Vorschläge offen
Das Design darf nicht zu überladen sein.

```html
<!DOCTYPE html>
<html lang="de">
<head>
<meta charset="utf-8">
<title>Das Licht am Ufer – Rupert(a) Hallmann</title>
<link rel="stylesheet" href="https://fonts.googleapis.com/css2?family=Abril+Fatface&family=Playfair+Display:wght@700;800&display=swap">
<style>
  :root {
    --stage: #ececec;
    --paper: #ffffff;
    --ink: #23282b;
    --band-teal: #0f4c66;
    --band-deep: #071c26;
    --band-black: #030607;
    --name: #ffffff;
    --portrait-light: #6f7c86;
    --portrait-dark: #141a1f;
  }
  * { margin: 0; padding: 0; box-sizing: border-box; }
  html, body {
    width: 1200px;
    height: 900px;
    overflow: hidden;
    background: var(--stage);
  }
  .book-cover {
    position: absolute;
    left: 310px;
    top: 0;
    width: 580px;
    height: 900px;
    background: var(--paper);
    overflow: hidden;
  }
  .title {
    position: absolute;
    inset: 0;
    font-family: "Abril Fatface", "Playfair Display", serif;
    color: var(--ink);
    font-weight: 400;
    font-size: 185px;
    line-height: 1;
    letter-spacing: -4px;
  }
  .title-line {
    position: absolute;
    left: 0;
    width: 100%;
    text-align: center;
    white-space: nowrap;
  }
  .title-line--1 { top: -7px; }
  .title-line--2 { top: 143px; }
  .title-line--3 { top: 258px; }
  .title-line--4 { top: 402px; }
  .band {
    position: absolute;
    left: 0;
    top: 600px;
    width: 580px;
    height: 300px;
  }
  .author-portrait {
    position: absolute;
    left: 322px;
    top: 604px;
    width: 156px;
    height: 124px;
    border-radius: 68px 68px 0 0;
    background: radial-gradient(ellipse at 50% 30%, var(--portrait-light) 0%, #3a444c 45%, var(--portrait-dark) 100%);
  }
  .author {
    position: absolute;
    left: 0;
    top: 706px;
    width: 100%;
    text-align: center;
    font-family: "Playfair Display", serif;
    font-weight: 800;
    color: var(--name);
    text-transform: uppercase;
    line-height: 1.0;
    font-size: 80px;
    letter-spacing: -1px;
  }
  .author-line { display: block; white-space: nowrap; }
</style>
</head>
<body>
  <main class="book-cover">
    <svg class="band" viewBox="0 0 580 300" aria-hidden="true">
      <defs>
        <linearGradient id="bandFill" x1="1" y1="0" x2="0.2" y2="1">
          <stop offset="0" stop-color="#0f4c66"/>
          <stop offset="0.45" stop-color="#071c26"/>
          <stop offset="0.8" stop-color="#030607"/>
        </linearGradient>
      </defs>
      <path d="M0 66 C 150 54, 260 32, 400 18 C 470 12, 530 8, 580 6 L580 300 L0 300 Z" fill="url(#bandFill)"/>
    </svg>

    <div class="author-portrait" role="img" aria-label="Porträtfoto des Autors in dunklem Sakko"></div>

    <h1 class="title">
      <span class="title-line title-line--1">Das</span>
      <span class="title-line title-line--2">Licht</span>
      <span class="title-line title-line--3">am</span>
      <span class="title-line title-line--4">Ufer</span>
    </h1>

    <p class="author">
      <span class="author-line">Rupert(a)</span>
      <span class="author-line">Hallmann</span>
    </p>
  </main>
</body>
</html>
```